Business Card Design

We need a design for business cards for our company. We have a logo. We teach EMT's and we are based out of Virginia. The information that will need to add would be, name, title, phone number, email, address. On the back of the business card would be "Train with us, care for all"

Target Market(s)

People that want to become EMT's

Colors

Designer to choose colors to be used in the design.

Requirements
Must have
• company logo

```html
<!DOCTYPE html>
<html lang="en">
<head>
<meta charset="utf-8">
<title>Ridgeline Medic Training – Business Card</title>
<link href="https://fonts.googleapis.com/css2?family=Lato:wght@300;400;700&family=Montserrat:wght@600&display=swap" rel="stylesheet">
<style>
  :root {
    --page: #1c1c1e;
    --card-dark: #1d2334;
    --card-mid: #262e44;
    --pattern: #2f3850;
    --red: #e8283a;
    --white: #f2f3f6;
    --muted: #c9ccd6;
  }
  * { margin: 0; padding: 0; box-sizing: border-box; }
  html, body { width: 1200px; height: 900px; overflow: hidden; }
  body {
    background: var(--page);
    font-family: "Lato", sans-serif;
    position: relative;
  }
  .card {
    position: absolute;
    left: 240px;
    width: 720px;
    height: 411px;
    background: linear-gradient(135deg, var(--card-mid) 0%, var(--card-dark) 70%);
    overflow: hidden;
    box-shadow: 0 10px 30px rgba(0,0,0,.5);
  }
  .card--front { top: 28px; }
  .card--back { top: 462px; }

  .cross-field {
    position: absolute;
    top: 0; right: 0;
    width: 300px; height: 100%;
    background: linear-gradient(250deg, var(--pattern) 0%, rgba(47,56,80,0) 80%);
  }

  .wordmark {
    position: absolute;
    display: flex;
    align-items: center;
    gap: 12px;
    font-family: "Montserrat", sans-serif;
    font-weight: 600;
    color: var(--red);
    letter-spacing: 1px;
    line-height: 1.05;
  }
  .wordmark__dot {
    width: 16px; height: 16px;
    border-radius: 50%;
    background: var(--red);
    flex: none;
  }
  .card--front .wordmark { left: 150px; top: 150px; font-size: 40px; }
  .card--back .wordmark { left: 250px; top: 70px; font-size: 30px; }

  .rule { position: absolute; background: var(--red); }
  .rule--front-left { left: 0; top: 318px; width: 250px; height: 2px; }
  .rule--front-right { right: 0; top: 318px; width: 200px; height: 2px; }
  .tagline {
    position: absolute;
    left: 262px; top: 309px;
    width: 250px;
    text-align: center;
    font-size: 15px;
    letter-spacing: .5px;
    color: var(--white);
    text-transform: uppercase;
    white-space: nowrap;
  }

  .rule--back-top { left: 44px; top: 0; width: 2px; height: 200px; }
  .rule--back-bottom { left: 44px; bottom: 0; width: 2px; height: 44px; }

  .contact {
    position: absolute;
    left: 52px; top: 222px;
    color: var(--white);
  }
  .contact__name { font-size: 22px; color: var(--red); letter-spacing: .5px; }
  .contact__first { font-weight: 700; }
  .contact__last { font-weight: 300; }
  .contact__title { font-size: 15px; font-weight: 700; margin: 2px 0 16px; }
  .contact__row {
    display: flex; align-items: center; gap: 12px;
    font-size: 15px; margin-bottom: 6px;
  }
  .contact__row svg { width: 14px; height: 14px; fill: var(--red); flex: none; }
  .contact__web { font-size: 16px; color: var(--red); margin-top: 4px; }
</style>
</head>
<body>

<section class="card card--front">
  <div class="cross-field" role="img" aria-label="Faint pattern of medical cross shapes"></div>
  <div class="wordmark"><span class="wordmark__dot"></span>RIDGELINE MEDIC TRAINING</div>
  <div class="rule rule--front-left"></div>
  <p class="tagline">Train with us, care for all</p>
  <div class="rule rule--front-right"></div>
</section>

<section class="card card--back">
  <div class="cross-field" role="img" aria-label="Faint pattern of medical cross shapes"></div>
  <div class="wordmark"><span class="wordmark__dot"></span>RIDGELINE MEDIC TRAINING</div>
  <div class="rule rule--back-top"></div>
  <div class="contact">
    <p class="contact__name"><span class="contact__first">DANA</span> <span class="contact__last">KESSLER</span></p>
    <p class="contact__title">Founder / Director</p>
    <p class="contact__row">
      <svg viewBox="0 0 24 24" aria-hidden="true"><path d="M6.6 10.8a15.1 15.1 0 0 0 6.6 6.6l2.2-2.2a1 1 0 0 1 1-.25 11.4 11.4 0 0 0 3.6.57 1 1 0 0 1 1 1V20a1 1 0 0 1-1 1A17 17 0 0 1 3 4a1 1 0 0 1 1-1h3.5a1 1 0 0 1 1 1c0 1.25.2 2.45.57 3.57a1 1 0 0 1-.25 1z"/></svg>
      +1 540 555 0142
    </p>
    <p class="contact__row">
      <svg viewBox="0 0 24 24" aria-hidden="true"><rect x="2" y="5" width="20" height="14" rx="1"/><path d="M3 6l9 7 9-7" fill="none" stroke="#1d2334" stroke-width="2"/></svg>
      info@ridgelinemedic.com
    </p>
    <p class="contact__web">www.ridgelinemedic.com</p>
  </div>
  <div class="rule rule--back-bottom"></div>
</section>

</body>
</html>
```